Fennick Medical - Flyer

We are a full service pharmacy that specializes in diabetic testing and medications. We research the patient's insurance to maximize their insurance benefit and then deliver the medications monthly directly to the patient's doorstep, for free! We save the patient, time and money every month.
We would love a flyer that we can distribute to Doctor's offices and patients that sum up our pharmacy. Emphasis on saving money, time, and getting the best quality supplies by maximizing their insurance. We want it to be eye catching, clean, and professional.
You can use our logo or feel free to make your own design.
diabetic patients wanting to save money
Insurance

```html
<!DOCTYPE html>
<html lang="en">
<head>
<meta charset="utf-8">
<title>Fennick Medical – Full Service Pharmacy Flyer</title>
<link rel="stylesheet" href="https://fonts.googleapis.com/css2?family=Anton&family=Arimo:ital,wght@0,400;1,400&display=swap">
<style>
  :root {
    --paper: #ffffff;
    --ink: #2b2b2b;
    --brand-green: #8cc63f;
    --band-green: #9fcd5e;
    --band-blue: #2aa9c6;
    --gold-light: #fff3c4;
    --gold-mid: #ffd36b;
    --gold-deep: #f6a623;
    --white: #ffffff;
  }
  html, body {
    margin: 0;
    padding: 0;
    overflow: hidden;
    background: var(--paper);
  }
  .flyer {
    position: relative;
    width: 800px;
    height: 1200px;
    overflow: hidden;
    background: var(--paper);
    font-family: "Arimo", Arial, sans-serif;
  }
  .brand {
    position: absolute;
    top: 62px;
    left: 0;
    width: 800px;
    display: flex;
    justify-content: center;
    align-items: center;
    gap: 18px;
    z-index: 2;
  }
  .brand-dot {
    width: 64px;
    height: 64px;
    border-radius: 50%;
    background: var(--brand-green);
  }
  .brand-name {
    color: var(--ink);
    font-weight: 400;
    line-height: 1;
    text-transform: uppercase;
  }
  .brand-name .line-1 {
    display: block;
    font-size: 62px;
    letter-spacing: 1px;
  }
  .brand-name .line-2 {
    display: block;
    font-size: 26px;
    letter-spacing: 15px;
    margin-top: 6px;
  }
  .hero-photo {
    position: absolute;
    top: 178px;
    left: 0;
    width: 800px;
    height: 524px;
    background:
      linear-gradient(180deg, rgba(255,255,255,0.95) 0%, rgba(255,255,255,0) 14%),
      linear-gradient(90deg, #b9d9a8 0%, #dfe8e2 30%, #eef1ef 55%, #e3e7e6 80%, #d2dccf 100%);
  }
  .delivery-badge {
    position: absolute;
    left: 550px;
    top: 486px;
    width: 166px;
    height: 166px;
    border-radius: 50%;
    background: radial-gradient(circle at 40% 35%, #b6dc6a 0%, #8cc63f 60%, #6fa82c 100%);
    box-shadow: 0 0 0 3px rgba(255,255,255,0.8);
    display: flex;
    align-items: center;
    justify-content: center;
    text-align: center;
    color: var(--white);
    font-family: "Anton", Impact, sans-serif;
    font-size: 25px;
    line-height: 1.05;
    text-shadow: 1px 2px 2px rgba(0,0,0,0.55);
  }
  .headline-band {
    position: absolute;
    top: 702px;
    left: 0;
    width: 800px;
    height: 294px;
    background: var(--band-green);
    text-align: center;
  }
  .headline {
    margin: 0;
    padding-top: 4px;
    font-family: "Anton", Impact, sans-serif;
    font-weight: 400;
    font-size: 146px;
    line-height: 142px;
    letter-spacing: 2px;
    background: linear-gradient(180deg, var(--gold-deep) 0%, var(--gold-mid) 45%, var(--gold-light) 100%);
    -webkit-background-clip: text;
    background-clip: text;
    color: transparent;
    filter: drop-shadow(3px 4px 3px rgba(0,0,0,0.4));
  }
  .headline span { display: block; }
  .info-band {
    position: absolute;
    top: 996px;
    left: 0;
    width: 800px;
    height: 204px;
    background: var(--band-blue);
    color: var(--white);
    text-align: center;
  }
  .specialty {
    margin: 14px 0 0;
    font-size: 20px;
    letter-spacing: 0.3px;
    text-transform: uppercase;
  }
  .insurance-note {
    margin: 4px 0 0;
    font-style: italic;
    font-size: 28px;
    line-height: 30px;
  }
  .tagline {
    margin: 6px 0 0;
    font-family: "Anton", Impact, sans-serif;
    font-weight: 400;
    font-size: 46px;
    letter-spacing: 1px;
    text-shadow: 2px 3px 3px rgba(0,0,0,0.45);
  }
</style>
</head>
<body>
  <main class="flyer">
    <header class="brand">
      <div class="brand-dot"></div>
      <div class="brand-name">
        <span class="line-1">Fennick</span>
        <span class="line-2">Medical</span>
      </div>
    </header>

    <div class="hero-photo" role="img" aria-label="Smiling pharmacist in a white coat writing on a clipboard at the pharmacy counter, shelves of medicine behind her"></div>

    <div class="delivery-badge">Free<br>Delivery<br>At Your<br>Doorstep</div>

    <section class="headline-band">
      <h1 class="headline"><span>Full Service</span><span>Pharmacy</span></h1>
    </section>

    <section class="info-band">
      <p class="specialty">Specializing in diabetic testing and medications.</p>
      <p class="insurance-note">We research the patient's insurance to maximize<br>their insurance benefits.</p>
      <p class="tagline">Saving Patients Time &amp; Money</p>
    </section>
  </main>
</body>
</html>
```